Quelto Marketing & Design needs a Wordpress website

We need a wordpress design for a new marketing and design company in Australia called 'Quelto Marketing & Design". The website needs to be responsive, modern, and attract new customers. It needs to be unique and different. We provide marketing and design solutions for small businesses from consulting, to flyer distribution to Facebook ads etc. We would like to see designs that use the Quelto logo colours. The final design should communicate professionalism, creativity & growth. It needs to stand out from the crowd.

Target Market(s)

Small Business who need a marketing freelancer to help them grow

Industry/Entity Type

Marketing

Number of Pages Required

3 page

Requirements
Must have
• Home page, services page & contact page

```html
<!DOCTYPE html>
<html lang="en">
<head>
<meta charset="utf-8">
<title>Quelto Marketing &amp; Design</title>
<link href="https://fonts.googleapis.com/css2?family=Open+Sans:wght@400;600;700&family=Raleway:wght@500;600;700&display=swap" rel="stylesheet">
<style>
:root{
  --plum:#4a1a45;
  --plum-dark:#2e1230;
  --magenta:#c2185b;
  --pink:#e0457f;
  --ink:#444;
  --muted:#777;
  --light:#f3f1f3;
  --line:#e2dde2;
  --white:#fff;
}
*{box-sizing:border-box;margin:0;padding:0}
html,body{width:1200px;height:2740px;overflow:hidden}
body{font-family:"Open Sans",Arial,sans-serif;color:var(--ink);background:var(--white);font-size:12px;line-height:1.6}
h1,h2,h3,h4{font-family:"Raleway","Open Sans",sans-serif;font-weight:600}
section,header,footer{overflow:hidden}
.wrap{width:960px;margin:0 auto;position:relative}

/* header */
.site-header{height:90px;background:var(--white);border-bottom:1px solid var(--line)}
.site-header .wrap{height:90px}
.brand{position:absolute;left:0;top:14px;display:flex;align-items:center;gap:10px}
.brand-mark{width:54px;height:54px;border-radius:50%;background:var(--magenta)}
.brand-name{font-family:"Raleway",sans-serif;font-size:34px;font-weight:700;color:var(--plum);line-height:1}
.brand-tag{font-size:10px;color:var(--magenta);letter-spacing:1px;margin-top:4px}
.top-contact{position:absolute;right:0;top:8px;font-size:11px;color:var(--muted);display:flex;gap:18px;align-items:center}
.flag{width:18px;height:12px;background:var(--magenta);display:inline-block}
.main-nav{position:absolute;right:0;top:52px;display:flex;gap:4px}
.main-nav a{font-size:13px;color:var(--ink);text-decoration:none;padding:6px 12px}
.main-nav a.active{border-bottom:3px solid var(--magenta);color:var(--plum)}

/* hero */
.hero{height:350px;position:relative;background:linear-gradient(90deg,#3a1236 0%,#6e2a64 45%,#9a4b8c 75%,#5e1e55 100%)}
.hero-photo{position:absolute;left:300px;top:0;width:300px;height:350px;background:linear-gradient(180deg,#8a5a7e,#4a2244)}
.hero-copy{position:absolute;left:640px;top:70px;width:340px;color:var(--white)}
.hero-copy h1{font-size:38px;font-weight:600;line-height:1.1;margin-bottom:14px;white-space:nowrap}
.hero-copy p{font-size:12px;opacity:.9;margin-bottom:18px;width:300px}
.btn{display:inline-block;background:var(--plum);color:var(--white);font-size:12px;padding:8px 18px;border-radius:2px;text-decoration:none}
.hero-arrow{position:absolute;top:160px;width:30px;height:30px}
.hero-arrow.left{left:20px}
.hero-arrow.right{right:20px}
.dots{position:absolute;bottom:18px;left:0;right:0;display:flex;justify-content:center;gap:8px}
.dots span{width:9px;height:9px;border-radius:50%;background:rgba(255,255,255,.5)}
.dots span.on{background:var(--white)}

/* sections */
.section-title{text-align:center;font-size:28px;color:var(--magenta);margin-bottom:6px}
.section-title strong{color:var(--plum);font-weight:600}
.rule{width:60px;height:2px;background:var(--magenta);margin:0 auto 16px}
.lead{text-align:center;color:var(--muted);font-size:12px;max-width:640px;margin:0 auto}

.welcome{height:160px;padding-top:22px}
.welcome h2{text-align:center;font-size:28px;color:var(--plum);margin-bottom:10px}
.welcome p{text-align:center;color:var(--muted);font-size:12px}

.services{height:450px;background:var(--light);padding-top:28px}
.service-grid{display:flex;justify-content:space-between;margin:28px 60px 24px}
.service{width:180px;text-align:center}
.service-icon{width:96px;height:96px;border-radius:50%;border:2px solid var(--magenta);margin:0 auto 14px;display:flex;align-items:center;justify-content:center}
.service h3{font-size:14px;color:var(--plum);margin-bottom:8px}
.service p{font-size:11px;color:var(--muted)}
.center{text-align:center}

.about{height:340px;position:relative;padding-top:30px;background:linear-gradient(180deg,#efe9ee,#ddd3dc)}
.about h3{text-align:center;font-size:14px;color:var(--plum);margin-bottom:10px}
.about p{text-align:justify;font-size:11px;color:#555;margin-bottom:18px;line-height:1.65}

.clients{height:500px;background:var(--light);padding-top:34px}
.testimonials{display:grid;grid-template-columns:1fr 1fr;gap:22px;margin-top:30px}
.card{background:var(--white);border:1px solid var(--line);height:150px;padding:26px 24px;display:flex;gap:22px}
.avatar{width:80px;height:80px;border-radius:50%;flex:none;background:linear-gradient(135deg,#b89a8e,#5c4740)}
.card p{font-size:11px;color:var(--muted);margin-bottom:10px}
.card .name{color:var(--magenta);font-size:11px;font-weight:600}

.partners{height:80px;display:flex;align-items:center;justify-content:center;gap:70px;border-bottom:1px solid var(--line)}
.partner{display:flex;align-items:center;gap:8px;font-family:"Open Sans",sans-serif;font-weight:600;font-size:18px;color:#888}
.partner i{width:14px;height:14px;background:#aaa;border-radius:50%;display:block}

/* map + form */
.contact{height:470px;position:relative;background:linear-gradient(135deg,#e6e4dc,#d9dccf 50%,#c7d7e3)}
.contact-form{position:absolute;left:420px;top:50px;width:360px;height:370px;background:rgba(46,18,48,.85);padding:30px;color:var(--white)}
.contact-form h2{font-size:20px;text-align:center;line-height:1.35;margin-bottom:22px}
.field{height:30px;background:var(--white);margin-bottom:10px;font-size:11px;color:#999;padding:7px 10px}
.field.tall{height:80px}
.contact-form .btn{display:block;width:110px;margin:14px auto 0;text-align:center;background:var(--magenta)}

/* footer */
.site-footer{height:260px;background:var(--plum-dark);color:#cdbfcc;padding-top:34px}
.footer-cols{display:flex;gap:34px}
.footer-col{width:160px;font-size:11px}
.footer-col.wide{width:250px}
.footer-col h4{color:var(--white);font-size:14px;margin-bottom:12px}
.footer-col li{list-style:none;margin-bottom:5px}
.footer-brand{display:flex;align-items:center;gap:8px;margin-bottom:12px}
.footer-brand .brand-mark{width:34px;height:34px}
.footer-brand span{font-family:"Raleway",sans-serif;font-size:20px;font-weight:700;color:var(--white)}
.post{display:flex;gap:10px;margin-bottom:12px}
.post-thumb{width:44px;height:36px;flex:none;background:#6a4a66}
.bottom-bar{height:40px;background:#1f0c21;color:#a894a5;font-size:10px}
.bottom-bar .wrap{height:40px;display:flex;align-items:center;justify-content:space-between}
.social{display:flex;gap:6px}
.social span{width:18px;height:18px;background:#5b3a58;display:block}
</style>
</head>
<body>

<header class="site-header">
  <div class="wrap">
    <div class="brand">
      <span class="brand-mark"></span>
      <div>
        <div class="brand-name">Quelto</div>
        <div class="brand-tag">MARKETING &amp; DESIGN</div>
      </div>
    </div>
    <div class="top-contact">
      <span>hello@queltomarketing.com.au</span>
      <span>+61 400 123 987</span>
      <span class="flag"></span>
    </div>
    <nav class="main-nav">
      <a href="#" class="active">Home</a>
      <a href="#">Services</a>
      <a href="#">About Us</a>
      <a href="#">Our Clients</a>
      <a href="#">Contact Us</a>
    </nav>
  </div>
</header>

<section class="hero">
  <div class="hero-photo" role="img" aria-label="Photo of a smiling businesswoman in a dark suit"></div>
  <div class="hero-copy">
    <h1>We Are With You</h1>
    <p>We help small businesses grow with smart marketing, fresh design and honest advice. From your first flyer to a full campaign, we stay beside you at every step of the journey.</p>
    <a class="btn" href="#">Learn More</a>
  </div>
  <svg class="hero-arrow left" viewBox="0 0 30 30"><path d="M19 6 L10 15 L19 24" stroke="#fff" stroke-width="3" fill="none"/></svg>
  <svg class="hero-arrow right" viewBox="0 0 30 30"><path d="M11 6 L20 15 L11 24" stroke="#fff" stroke-width="3" fill="none"/></svg>
  <div class="dots"><span class="on"></span><span></span><span></span></div>
</section>

<section class="welcome">
  <div class="wrap">
    <h2>Welcome to Quelto Marketing &amp; Design</h2>
    <p>Quelto is a friendly marketing and design studio built for small businesses across Australia. We believe every local business deserves a brand that looks sharp and a plan that brings real customers through the door. Our team blends creative design with practical marketing, so your logo, flyers, website and social ads all work together. Whether you need a one-off project or a long-term partner, we tailor each solution to your goals, your budget and your market, and we measure the results so you can see your business grow month after month.</p>
  </div>
</section>

<section class="services">
  <div class="wrap">
    <h2 class="section-title">Our <strong>Services</strong></h2>
    <div class="rule"></div>
    <p class="lead">Marketing and design services shaped for small businesses. Whatever stage you are at, we can help you stand out, reach more people and grow.</p>
    <div class="service-grid">
      <div class="service">
        <div class="service-icon"><svg width="44" height="44" viewBox="0 0 44 44" fill="none" stroke="#c2185b" stroke-width="2"><path d="M8 36 L30 14 L36 20 L14 42Z"/><path d="M30 14 L34 6 L40 12 L36 20"/></svg></div>
        <h3>Logo Design</h3>
        <p>Distinctive logos that capture who you are and make your business easy to remember.</p>
      </div>
      <div class="service">
        <div class="service-icon"><svg width="44" height="44" viewBox="0 0 44 44" fill="none" stroke="#c2185b" stroke-width="2"><rect x="6" y="10" width="32" height="24" rx="2"/><circle cx="16" cy="20" r="4"/><path d="M24 18h10M24 24h10M10 30h24"/></svg></div>
        <h3>Corporate Identity</h3>
        <p>Business cards, letterheads and brand guides that keep every touchpoint consistent.</p>
      </div>
      <div class="service">
        <div class="service-icon"><svg width="44" height="44" viewBox="0 0 44 44" fill="none" stroke="#c2185b" stroke-width="2"><rect x="10" y="6" width="24" height="32"/><path d="M15 14h14M15 20h14M15 26h9"/></svg></div>
        <h3>Flyers</h3>
        <p>Eye-catching flyers designed, printed and delivered straight to your local area.</p>
      </div>
      <div class="service">
        <div class="service-icon"><svg width="44" height="44" viewBox="0 0 44 44" fill="none" stroke="#c2185b" stroke-width="2"><circle cx="16" cy="16" r="6"/><path d="M6 36c0-7 4-11 10-11s10 4 10 11"/><path d="M26 8h14v10h-6l-4 4v-4h-4z"/></svg></div>
        <h3>Consulting</h3>
        <p>Clear, practical advice to plan campaigns, social ads and your next growth step.</p>
      </div>
    </div>
    <div class="center"><a class="btn" href="#">See More</a></div>
  </div>
</section>

<section class="about" role="img" aria-label="Faded photo of a modern office behind the About Us text">
  <div class="wrap">
    <h2 class="section-title">About <strong>Us</strong></h2>
    <div class="rule"></div>
    <h3>Who is Quelto Marketing &amp; Design?</h3>
    <p>Quelto Marketing &amp; Design started with a simple idea: small businesses deserve the same quality of marketing as big brands, without the big agency price tag. We are a small team of designers, writers and marketers who love helping local owners tell their story. Over the years we have worked with cafes, trades, clinics, retailers and startups, building brands from scratch and refreshing tired ones. We listen first, then plan a mix of design and marketing that suits your customers and your budget. Our work covers logos and identity, printed flyers and their distribution, websites, social media content and paid ads on the platforms your audience uses most. Every project is handled personally, with clear timelines and honest reporting, so you always know what is happening and why. We measure results and adjust as we go, because growth comes from steady improvement rather than guesswork. When you work with Quelto you gain a creative partner who cares about your success as much as you do, and who is ready to help you stand out from the crowd in a busy market.</p>
    <div class="center"><a class="btn" href="#">See More</a></div>
  </div>
</section>

<section class="clients">
  <div class="wrap">
    <h2 class="section-title">Our <strong>Clients</strong></h2>
    <div class="rule"></div>
    <p class="lead">Here is what some of the businesses we work with have to say about us.</p>
    <div class="testimonials">
      <div class="card">
        <div class="avatar" role="img" aria-label="Portrait photo of a client"></div>
        <div><p>Quelto gave our bakery a fresh new look and a flyer campaign that filled our shop on opening weekend. Friendly, fast and full of ideas we had never thought of.</p><div class="name">Mia Castell, Owner</div></div>
      </div>
      <div class="card">
        <div class="avatar" role="img" aria-label="Portrait photo of a client"></div>
        <div><p>Our social ads finally bring in real enquiries. The team explained every step clearly and the monthly reports show exactly where our new customers are coming from.</p><div class="name">Daniel Hart, Director</div></div>
      </div>
      <div class="card">
        <div class="avatar" role="img" aria-label="Portrait photo of a client"></div>
        <div><p>From logo to business cards to website, everything now feels like one brand. Clients tell us we look like a much bigger company than we are.</p><div class="name">Owen Rakes, Founder</div></div>
      </div>
      <div class="card">
        <div class="avatar" role="img" aria-label="Portrait photo of a client"></div>
        <div><p>Great value and genuine care. Quelto helped us plan a year of marketing that fits our budget, and our bookings have grown every single month since.</p><div class="name">Lena Fordham, Manager</div></div>
      </div>
    </div>
  </div>
</section>

<div class="partners">
  <span class="partner"><i></i>Stemwell</span>
  <span class="partner">Loomra</span>
  <span class="partner">Yelmora</span>
  <span class="partner">Searchly</span>
  <span class="partner"><i></i>Townfind</span>
</div>

<section class="contact" role="img" aria-label="Street map of the city around the studio location">
  <div class="contact-form">
    <h2>We'd love to hear from you so why don't you get in touch?</h2>
    <div class="field">Name</div>
    <div class="field">Email</div>
    <div class="field">Phone</div>
    <div class="field tall">Message</div>
    <a class="btn" href="#">Submit</a>
  </div>
</section>

<footer class="site-footer">
  <div class="wrap footer-cols">
    <div class="footer-col">
      <div class="footer-brand"><span class="brand-mark"></span><span>Quelto</span></div>
      <p>Quelto Marketing &amp; Design<br>12 Harbour Lane, Suite 4<br>Brisbane QLD 4000</p>
    </div>
    <div class="footer-col">
      <h4>Quick Links</h4>
      <ul><li>Home</li><li>Services</li><li>About Us</li><li>Our Clients</li><li>Contact Us</li></ul>
    </div>
    <div class="footer-col">
      <h4>Contact One</h4>
      <ul><li>Phone: +61 400 123 987</li><li>Email: hello@queltomarketing.com.au</li><li>Mon – Fri, 9am – 5pm</li></ul>
    </div>
    <div class="footer-col">
      <h4>Contact Two</h4>
      <ul><li>Phone: +61 400 456 210</li><li>Email: studio@queltomarketing.com.au</li><li>Sat, 10am – 2pm</li></ul>
    </div>
    <div class="footer-col wide">
      <h4>From the Blog</h4>
      <div class="post"><span class="post-thumb"></span><span>Five simple ways to make your flyers work harder for you</span></div>
      <div class="post"><span class="post-thumb"></span><span>How small budgets can win big with social ads this year</span></div>
      <div class="post"><span class="post-thumb"></span><span>Why a clear brand helps local customers trust you faster</span></div>
    </div>
  </div>
</footer>
<div class="bottom-bar">
  <div class="wrap">
    <span>Copyright © 2024 Quelto Marketing &amp; Design. All rights reserved.</span>
    <div class="social"><span></span><span></span><span></span><span></span></div>
  </div>
</div>

</body>
</html>
```